Biodegradable wooden cutlery needs packaging

We need a cardboard packaging design for earth friendly wooden cutlery. Our brand is called Meadow Basket. The cutlery is made of 100% natural birch wood, each set comes with 50 spoons, 50 knives and 100 forks. Costumers are attracted to this product because it is: biodegradable, sustainable, reduces waste, and is sturdier than plastic cutlery. The box size will be 230*185*55mm.

The final design should communicate that the product is earth friendly, sustainable, and high quality. We are looking for a design which gets these points across while remaining SIMPLE.

PLEASE SEE ALL ATTACHMENTS AND PAY ATTENTION TO WHERE BOX PRINTING LOCATIONS

Target Market(s)

People who are eco conscious, people who have barbecues/picnics, people concerned about plastic waste and pollution

Industry/Entity Type

Online Shopping

Colors
33b8a4
86cfc6
abd037
cadf82
fbf289
fbee3e
35a7d7

Requirements
Must have
• Name on front of box. (see attachments)
• Barcode on the side of the box (see attachments)
• Must say "Made in China" on box
• Must make use of brown cardboard background, and not use printed background colour all over box.
Nice to have
• Trees or leaves (I will leave to your discretion). We want the costumer to be thinking natural and eco friendly.
• Note: colour preferences are just suggestions, feel free to add or remove as you see fit. Please try to use 2 colours.
Should not have
• Overly complex or busy

```html
<!DOCTYPE html>
<html lang="en">
<head>
<meta charset="utf-8">
<title>Meadow Basket – Wooden Cutlery Mailer Box Dieline</title>
<link rel="stylesheet" href="https://fonts.googleapis.com/css2?family=Montserrat:wght@300;500&display=swap">
<style>
  :root {
    --backdrop: #d6d6d6;
    --kraft: #d9ab5e;
    --kraft-edge: #c99a4f;
    --crease: #c4954c;
    --forest: #3b4414;
    --leaf: #8f9a3a;
    --leaf-soft: #a7a548;
    --ink: #2f3510;
    --gold-print: #c9a25a;
  }
  html, body {
    margin: 0;
    padding: 0;
    width: 1200px;
    height: 900px;
    overflow: hidden;
    background: var(--backdrop);
  }
  .dieline {
    display: block;
    width: 1200px;
    height: 900px;
  }
  .board { fill: var(--kraft); }
  .crease { stroke: var(--crease); stroke-width: 2; fill: none; }
  .base-print { fill: var(--forest); }
  .lid-artwork { fill: var(--leaf-soft); opacity: 0.55; }
  .base-artwork { fill: var(--gold-print); opacity: 0.45; }
  .brand-name {
    font-family: "Montserrat", sans-serif;
    font-weight: 500;
    font-size: 46px;
    fill: var(--ink);
  }
  .brand-name--base { fill: var(--gold-print); }
  .feature-list {
    font-family: "Montserrat", sans-serif;
    font-weight: 500;
    font-size: 11.5px;
    fill: var(--ink);
  }
  .feature-dot { fill: var(--ink); }
  .set-title {
    font-family: "Montserrat", sans-serif;
    font-weight: 300;
    font-size: 29px;
    fill: var(--ink);
    letter-spacing: -0.5px;
  }
</style>
</head>
<body>
<svg class="dieline" viewBox="0 0 1500 1125" xmlns="http://www.w3.org/2000/svg">

  <!-- lid tuck flap -->
  <path class="board" d="M445 130 L445 90 Q445 68 470 68 L990 68 Q1068 68 1068 110 L1068 130 Z"/>
  <!-- lid panel with side dust-flap notches -->
  <path class="board" d="M445 130 L1068 130 L1068 150 L1080 158 L1080 490 L1068 510 L1085 510 L1085 595 L430 595 L430 510 L448 510 L437 490 L437 158 L445 150 Z"/>
  <!-- base print panel -->
  <rect class="base-print" x="520" y="598" width="475" height="327"/>
  <!-- left side wall and flap -->
  <path class="board" d="M520 598 L520 925 L330 925 L330 835 L318 830 L318 700 L330 695 L330 603 Z"/>
  <!-- right side wall and flap -->
  <path class="board" d="M995 598 L995 925 L1188 925 L1188 835 L1198 830 L1198 700 L1188 695 L1188 603 Z"/>
  <!-- front wall -->
  <path class="board" d="M440 925 L1075 925 L1075 1000 L440 1000 Z"/>
  <!-- tab slots -->
  <rect x="520" y="692" width="13" height="140" fill="var(--backdrop)"/>
  <rect x="982" y="692" width="13" height="140" fill="var(--backdrop)"/>

  <!-- creases -->
  <line class="crease" x1="445" y1="130" x2="1068" y2="130"/>
  <line class="crease" x1="430" y1="595" x2="1085" y2="595"/>
  <line class="crease" x1="430" y1="510" x2="1085" y2="510"/>
  <line class="crease" x1="430" y1="600" x2="430" y2="925"/>
  <line class="crease" x1="1088" y1="600" x2="1088" y2="925"/>
  <line class="crease" x1="440" y1="940" x2="1075" y2="940"/>

  <!-- lid: leafy heart wreath artwork area -->
  <path class="lid-artwork" role="img" aria-label="Heart-shaped wreath of hand-drawn green leaves and branches"
        d="M752 470 C690 420 590 360 582 270 C576 200 640 160 700 175 C730 182 748 200 752 215 C758 195 790 165 840 165 C900 165 930 215 922 280 C912 360 815 425 752 470 Z"/>
  <text class="brand-name" x="752" y="320" text-anchor="middle">Meadow Basket</text>

  <!-- lid: feature list -->
  <g class="feature-list">
    <circle class="feature-dot" cx="553" cy="431" r="2.5"/>
    <text x="562" y="435">Made of 100 %</text>
    <text x="562" y="445">natural birch wood</text>
    <circle class="feature-dot" cx="553" cy="462" r="2.5"/>
    <text x="562" y="466">Thick, sturdy, high quality</text>
    <circle class="feature-dot" cx="553" cy="482" r="2.5"/>
    <text x="562" y="486">Earth friendly</text>
    <circle class="feature-dot" cx="553" cy="502" r="2.5"/>
    <text x="562" y="506">100% biodegradable</text>
  </g>

  <!-- lid: set title -->
  <g class="set-title" text-anchor="end">
    <text x="965" y="455">200-PIECE</text>
    <text x="965" y="480">WOODEN</text>
    <text x="965" y="505">CUTLERY SET</text>
  </g>

  <!-- base: inverted wreath artwork area -->
  <g transform="rotate(180 757 760)">
    <path class="base-artwork" role="img" aria-label="Heart-shaped wreath of hand-drawn leaves printed in kraft tone"
          d="M757 870 C705 830 625 785 632 715 C637 668 685 645 725 655 C745 660 755 672 757 682 C762 668 785 650 818 652 C865 655 888 690 880 730 C870 790 805 830 757 870 Z"/>
    <text class="brand-name brand-name--base" x="757" y="770" text-anchor="middle" font-size="38">Meadow Basket</text>
  </g>
</svg>
</body>
</html>
```